BRPS Postcard Design: Mosquito Control, Lawn Maintenance and Pressure washing

I have a new company based in Atlanta,Georgia named Brookvale Pest Shield Services, LLC. We specializes in Mosquito Control. We also have additional services: Lawn maintenance, Pressure Washing and Gutter Cleaning. I would like to see designs with the colors Black, Red, Gray. We would like the customer to think of us when it comes to Enjoying a mosquito free yard and improving the look and feel of their home and lawn.

Industry/Entity Type

It Company

Requirements
Nice to have
• Treatment plans starting at $69/mt - front of card
• The additional services we offer - back of card.

```html
<!DOCTYPE html>
<html lang="en">
<head>
<meta charset="utf-8">
<title>Brookvale Pest Shield Services – Mosquito Control Postcard</title>
<link rel="stylesheet" href="https://fonts.googleapis.com/css2?family=Montserrat:wght@300;600&family=Roboto+Condensed:wght@700&display=swap">
<style>
  :root {
    --red-bright: #d9343a;
    --red-mid: #a9161c;
    --red-deep: #3a0507;
    --black: #000000;
    --white: #ffffff;
    --ink: #0d0d0d;
    --silver-light: #f4f4f4;
    --silver-dark: #9b9b9b;
    --brand-red: #e0272d;
  }
  * { margin: 0; padding: 0; box-sizing: border-box; }
  html, body { width: 1200px; height: 778px; overflow: hidden; background: var(--black); }
  .postcard { position: relative; width: 1200px; height: 778px; overflow: hidden; font-family: "Montserrat", sans-serif; }

  .hero {
    position: absolute; left: 0; top: 0; width: 1200px; height: 537px;
    background:
      radial-gradient(ellipse 620px 380px at 52% 48%, var(--red-bright) 0%, var(--red-mid) 55%, transparent 100%),
      linear-gradient(90deg, var(--red-deep) 0%, var(--red-mid) 30%, var(--red-mid) 70%, var(--red-deep) 100%);
  }

  .headline-banner { position: absolute; left: 212px; top: 65px; width: 776px; height: 206px; }
  .headline-banner svg { position: absolute; inset: 0; }
  .headline-kicker {
    position: absolute; left: 0; width: 700px; top: 17px; text-align: center;
    font-size: 21px; font-weight: 600; color: var(--ink); letter-spacing: -0.2px;
  }
  .headline-title {
    position: absolute; left: 0; width: 700px; top: 46px; text-align: center;
    font-family: "Roboto Condensed", sans-serif; font-weight: 700;
    font-size: 76px; line-height: 74px; color: var(--ink); text-transform: uppercase;
  }

  .tagline {
    position: absolute; right: 763px; top: 358px; text-align: right;
    font-size: 38px; font-weight: 600; line-height: 50px; color: var(--white); letter-spacing: -0.5px;
  }
  .divider { position: absolute; top: 304px; width: 2px; height: 212px; background: var(--white); }
  .divider--left { left: 461px; }
  .divider--right { left: 739px; }

  .price { position: absolute; left: 463px; width: 276px; top: 318px; text-align: center; color: var(--white); }
  .price-amount { font-size: 128px; font-weight: 600; line-height: 140px; letter-spacing: -4px; }
  .price-note { font-size: 22px; font-weight: 300; margin-top: -2px; }

  .pitch {
    position: absolute; left: 765px; top: 320px; width: 400px;
    font-size: 21.5px; font-weight: 300; line-height: 32px; color: var(--white);
  }

  .footer {
    position: absolute; left: 0; top: 537px; width: 1200px; height: 241px;
    background: var(--black); text-align: center;
  }
  .brand-name {
    position: absolute; left: 0; width: 1200px; top: 62px;
    font-family: "Roboto Condensed", sans-serif; font-weight: 700;
    font-size: 48px; color: var(--white);
  }
  .brand-phone {
    position: absolute; left: 0; width: 1200px; top: 145px;
    font-family: "Roboto Condensed", sans-serif; font-weight: 700;
    font-size: 56px; letter-spacing: 2px; color: var(--brand-red);
  }
</style>
</head>
<body>
<div class="postcard">
  <section class="hero">
    <div class="headline-banner">
      <svg width="776" height="206" viewBox="0 0 776 206" aria-hidden="true">
        <defs>
          <linearGradient id="silver" x1="0" y1="0" x2="1" y2="0">
            <stop offset="0" stop-color="var(--silver-dark)"/>
            <stop offset="0.12" stop-color="var(--silver-light)"/>
            <stop offset="0.5" stop-color="#c9c9c9"/>
            <stop offset="0.85" stop-color="var(--silver-light)"/>
            <stop offset="1" stop-color="#d8d8d8"/>
          </linearGradient>
        </defs>
        <polygon points="0,0 676,0 776,103 676,206 0,206" fill="url(#silver)"/>
      </svg>
      <p class="headline-kicker">Brookvale Pest Shield Services Dedicated to</p>
      <h1 class="headline-title">Controlling<br>Mosquitos!</h1>
    </div>

    <p class="tagline">Enjoy A Mosquito<br>Free Yard</p>
    <span class="divider divider--left"></span>
    <div class="price">
      <div class="price-amount">$69</div>
      <div class="price-note">PER MONTH SPECIAL</div>
    </div>
    <span class="divider divider--right"></span>
    <p class="pitch">We are dedicated to controlling those pesky little mosquitos while helping you maintain your lawn and home. Call us today to find out about our great monthly specials.</p>
  </section>

  <footer class="footer">
    <p class="brand-name">Brookvale Pest Shield Services, LLC</p>
    <p class="brand-phone">404-555-0182</p>
  </footer>
</div>
</body>
</html>
```